Logo and animation for a set-top box for IPTV

We manufacture a set top box for IPTV. We need a better looking new boot up sequence. The process looks like that:
1. Logo (KV520/KV620/KV720) (needed in bot raster and vector)
2. "Loading" - here we want to have some kind of a better looking picture and and animation that consist of 30 frames- 30 separated image files.
3. "Waiting for network" screen should be changed to be with same design of the previous two screens. We must keep the bottom text too.

All images are 1920х1080

Attaching our current images.

As on the attached pictures.

```html
<!DOCTYPE html>
<html lang="en">
<head>
<meta charset="utf-8">
<title>Waiting for Network</title>
<link rel="stylesheet" href="https://fonts.googleapis.com/css2?family=Mulish:wght@500&family=Fira+Sans:ital,wght@1,500&display=swap">
<style>
  :root {
    --sky-top: #0b1446;
    --band-black: #05060c;
    --panel-top: #0f2f5e;
    --panel-bottom: #0a1d44;
    --floor-dark: #05070f;
    --rail-blue: #4a5ee0;
    --stage-blue: #2f56b6;
    --stage-light: #5b84d8;
    --text-white: #ffffff;
    --spinner: #e8ecf4;
  }
  * { margin: 0; padding: 0; box-sizing: border-box; }
  html, body { width: 1200px; height: 675px; overflow: hidden; background: var(--band-black); }
  .screen { position: relative; width: 1200px; height: 675px; overflow: hidden;
    background: linear-gradient(180deg, var(--sky-top) 0, var(--sky-top) 22px, var(--band-black) 22px, var(--band-black) 36px, var(--floor-dark) 36px); }
  .wall { position: absolute; left: 0; top: 36px; width: 1200px; height: 495px;
    background: linear-gradient(180deg, var(--panel-top), var(--panel-bottom)); }
  .thumb { position: absolute; opacity: 0.55; filter: blur(0.6px); }
  .thumb.faint { opacity: 0.22; }
  .spinner { position: absolute; left: 554px; top: 194px; }
  .status { position: absolute; left: 0; width: 1200px; top: 365px; text-align: center;
    font-family: "Mulish", sans-serif; font-weight: 500; font-size: 83px; letter-spacing: 1px;
    color: var(--text-white); text-shadow: 0 2px 6px rgba(0,0,0,0.5); line-height: 1; }
  .stage { position: absolute; left: 0; top: 531px; }
  .hint { position: absolute; left: 0; width: 1200px; top: 620px; display: flex; justify-content: center; align-items: center; gap: 10px;
    font-family: "Fira Sans", sans-serif; font-style: italic; font-weight: 500; font-size: 30px; color: var(--text-white);
    text-shadow: 0 2px 4px rgba(0,0,0,0.6); }
  .hint svg { flex: none; }
</style>
</head>
<body>
<main class="screen">
  <div class="wall"></div>

  <!-- gallery row 1 -->
  <div class="thumb" role="img" aria-label="Butterfly on a yellow flower" style="left:95px;top:73px;width:79px;height:63px;background:linear-gradient(135deg,#4f7a3a,#9cae6a)"></div>
  <div class="thumb" role="img" aria-label="Couple at sunset by the sea" style="left:211px;top:73px;width:106px;height:63px;background:linear-gradient(180deg,#6a5a5a,#c8874a,#3a2a2a)"></div>
  <div class="thumb" role="img" aria-label="Mountain lake through trees" style="left:355px;top:73px;width:84px;height:63px;background:linear-gradient(180deg,#7ea7d8,#5d7a5a)"></div>
  <div class="thumb" role="img" aria-label="Green hills over a rocky field" style="left:476px;top:73px;width:95px;height:63px;background:linear-gradient(180deg,#9aa8b0,#4b5a3a,#8a7a6a)"></div>
  <div class="thumb" role="img" aria-label="Aerial view of coastal farmland" style="left:609px;top:73px;width:113px;height:63px;background:linear-gradient(180deg,#b39a5a,#6a7a3a,#2a5a4a)"></div>
  <div class="thumb" role="img" aria-label="Whitewashed hillside town" style="left:759px;top:73px;width:95px;height:63px;background:linear-gradient(180deg,#6fa0e0,#d8c8b8,#b07a5a)"></div>
  <div class="thumb" role="img" aria-label="Off-road vehicle in a forest" style="left:891px;top:73px;width:95px;height:63px;background:linear-gradient(180deg,#5a5a5a,#3a3a3a)"></div>
  <div class="thumb" role="img" aria-label="Mountain above a lake" style="left:1024px;top:73px;width:85px;height:63px;background:linear-gradient(180deg,#8ab0e0,#7a6a5a,#2a5a9a)"></div>

  <!-- gallery row 2 -->
  <div class="thumb" role="img" aria-label="Curved beach under clouds" style="left:95px;top:171px;width:94px;height:64px;background:linear-gradient(180deg,#b8c8d8,#4a7aa0)"></div>
  <div class="thumb" role="img" aria-label="Mountain lake through trees" style="left:229px;top:171px;width:84px;height:64px;background:linear-gradient(180deg,#7ea7d8,#5d7a5a)"></div>
  <div class="thumb" role="img" aria-label="Windmill against a cloudy sky" style="left:353px;top:171px;width:95px;height:64px;background:linear-gradient(180deg,#8ab8e8,#e0e8f0,#6a6a6a)"></div>
  <div class="thumb" role="img" aria-label="Birds over a calm shore" style="left:488px;top:171px;width:96px;height:64px;background:linear-gradient(180deg,#c8a878,#a08a6a)"></div>
  <div class="thumb" role="img" aria-label="Mountain above a lake" style="left:624px;top:171px;width:94px;height:64px;background:linear-gradient(180deg,#8ab0e0,#7a6a5a,#2a5a9a)"></div>
  <div class="thumb" role="img" aria-label="Golden sunset over the sea" style="left:759px;top:171px;width:95px;height:64px;background:linear-gradient(180deg,#d09a3a,#b07a2a,#3a2a1a)"></div>
  <div class="thumb" role="img" aria-label="Curved beach under clouds" style="left:894px;top:171px;width:94px;height:64px;background:linear-gradient(180deg,#b8c8d8,#4a7aa0)"></div>
  <div class="thumb" role="img" aria-label="Mountain lake through trees" style="left:1029px;top:171px;width:83px;height:64px;background:linear-gradient(180deg,#7ea7d8,#5d7a5a)"></div>

  <!-- gallery row 3 -->
  <div class="thumb" role="img" aria-label="Golden sunset over the sea" style="left:94px;top:291px;width:95px;height:64px;background:linear-gradient(180deg,#d09a3a,#b07a2a,#3a2a1a)"></div>
  <div class="thumb" role="img" aria-label="Figures on a misty beach" style="left:247px;top:291px;width:95px;height:64px;background:linear-gradient(180deg,#7a9ab8,#4a6a8a,#6a6a6a)"></div>
  <div class="thumb" role="img" aria-label="Cargo ship at a harbour" style="left:400px;top:291px;width:94px;height:64px;background:linear-gradient(180deg,#8a9ab0,#4a7a6a,#5a5a6a)"></div>
  <div class="thumb" role="img" aria-label="Curved beach under clouds" style="left:553px;top:291px;width:94px;height:64px;background:linear-gradient(180deg,#b8c8d8,#4a7aa0)"></div>
  <div class="thumb" role="img" aria-label="Mountain lake through trees" style="left:706px;top:291px;width:84px;height:64px;background:linear-gradient(180deg,#7ea7d8,#5d7a5a)"></div>
  <div class="thumb" role="img" aria-label="Green hills over a rocky field" style="left:847px;top:291px;width:95px;height:64px;background:linear-gradient(180deg,#9aa8b0,#4b5a3a,#8a7a6a)"></div>
  <div class="thumb" role="img" aria-label="Aerial view of coastal farmland" style="left:1000px;top:291px;width:113px;height:64px;background:linear-gradient(180deg,#b39a5a,#6a7a3a,#2a5a4a)"></div>

  <!-- gallery row 4 -->
  <div class="thumb" role="img" aria-label="Grassy hillside with rocks" style="left:95px;top:386px;width:100px;height:69px;background:linear-gradient(180deg,#5a8a4a,#8a9a8a)"></div>
  <div class="thumb faint" role="img" aria-label="Forest scene" style="left:253px;top:386px;width:97px;height:69px;background:linear-gradient(180deg,#3a6a4a,#2a4a3a)"></div>
  <div class="thumb faint" role="img" aria-label="Landscape scene" style="left:409px;top:386px;width:97px;height:69px;background:linear-gradient(180deg,#5a7a8a,#3a5a6a)"></div>
  <div class="thumb faint" role="img" aria-label="Landscape scene" style="left:562px;top:386px;width:100px;height:69px;background:linear-gradient(180deg,#5a8aa0,#3a6a5a)"></div>
  <div class="thumb faint" role="img" aria-label="Landscape scene" style="left:719px;top:386px;width:100px;height:69px;background:linear-gradient(180deg,#4a7a9a,#3a5a5a)"></div>
  <div class="thumb faint" role="img" aria-label="Forest scene" style="left:875px;top:386px;width:100px;height:69px;background:linear-gradient(180deg,#3a8a5a,#2a5a3a)"></div>
  <div class="thumb" role="img" aria-label="Coastal rocks at dusk" style="left:1012px;top:386px;width:100px;height:69px;background:linear-gradient(180deg,#6a7a8a,#4a5a6a)"></div>

  <svg class="spinner" width="130" height="130" viewBox="0 0 130 130" aria-hidden="true">
    <defs>
      <linearGradient id="spin-fade" x1="0" y1="0" x2="1" y2="1">
        <stop offset="0" stop-color="#e8ecf4" stop-opacity="0"/>
        <stop offset="0.5" stop-color="#e8ecf4" stop-opacity="0.8"/>
        <stop offset="1" stop-color="#e8ecf4"/>
      </linearGradient>
    </defs>
    <path d="M65 4 A61 61 0 1 1 12 95" fill="none" stroke="url(#spin-fade)" stroke-width="5" stroke-linecap="round"/>
  </svg>

  <h1 class="status">WAITING FOR NETWORK</h1>

  <svg class="stage" width="1200" height="144" viewBox="0 0 1200 144" aria-hidden="true">
    <defs>
      <linearGradient id="floor-tiles" x1="0" y1="0" x2="0" y2="1">
        <stop offset="0" stop-color="#141a30"/>
        <stop offset="1" stop-color="#070a14"/>
      </linearGradient>
      <linearGradient id="rail" x1="0" y1="0" x2="1" y2="0">
        <stop offset="0" stop-color="#3a4ed0"/>
        <stop offset="0.6" stop-color="#6a7ae8"/>
        <stop offset="1" stop-color="#b8c0f0"/>
      </linearGradient>
      <radialGradient id="stage-glow" cx="0.5" cy="0.6" r="0.6">
        <stop offset="0" stop-color="#6c95e6"/>
        <stop offset="0.6" stop-color="#2f56b6"/>
        <stop offset="1" stop-color="#142a6a"/>
      </radialGradient>
    </defs>
    <rect x="0" y="0" width="1200" height="50" fill="url(#floor-tiles)"/>
    <g fill="none" stroke="#1e2848" stroke-width="1">
      <path d="M0 8 H1200 M0 18 H1200"/>
      <path d="M118 18 V50 M290 18 V50 M470 8 V50 M650 18 V50 M840 8 V50 M1020 18 V50"/>
    </g>
    <rect x="0" y="52" width="1200" height="4" fill="url(#rail)"/>
    <rect x="0" y="56" width="1200" height="88" fill="#04060c"/>
    <ellipse cx="620" cy="150" rx="720" ry="88" fill="#b8c0e0" opacity="0.35"/>
    <ellipse cx="560" cy="154" rx="640" ry="84" fill="url(#stage-glow)"/>
    <path d="M1040 80 Q1190 100 1185 144" fill="none" stroke="#d8def4" stroke-width="3" opacity="0.7"/>
  </svg>

  <p class="hint">
    <span>Press SETUP</span>
    <svg width="46" height="46" viewBox="0 0 46 46" aria-hidden="true">
      <g fill="#ffffff" transform="translate(23 23)">
        <rect x="-5" y="-22" width="10" height="10" rx="1"/>
        <rect x="-5" y="-22" width="10" height="10" rx="1" transform="rotate(45)"/>
        <rect x="-5" y="-22" width="10" height="10" rx="1" transform="rotate(90)"/>
        <rect x="-5" y="-22" width="10" height="10" rx="1" transform="rotate(135)"/>
        <rect x="-5" y="-22" width="10" height="10" rx="1" transform="rotate(180)"/>
        <rect x="-5" y="-22" width="10" height="10" rx="1" transform="rotate(225)"/>
        <rect x="-5" y="-22" width="10" height="10" rx="1" transform="rotate(270)"/>
        <rect x="-5" y="-22" width="10" height="10" rx="1" transform="rotate(315)"/>
        <circle r="15"/>
      </g>
      <circle cx="23" cy="23" r="7" fill="#3a62c0"/>
    </svg>
    <span>for settings</span>
  </p>
</main>
</body>
</html>
```